Plumbing Trifold Design for Restoration Company

We would like this brochure to match our current KVT branding and marketing materials. The overall look should feel modern, clean, premium, and trustworthy.

Our brand colors are included in the attached files along with a picture of what our current marketing material looks like. We'd like to use real KVT photography whenever possible rather than stock images, but if stock images are necessary, please go ahead and use.

The brochure should communicate that KVT is a full-service plumbing company backed by years of experience in both traditional plumbing and complex pipe restoration.

Front Page: we would like to include logo, phone number (800-318-4957), website (www.kvtflow.example) and then maybe the following: "Traditional Plumbing Services", "residential & commercial, 24/7 Emergency Service, Licensed & Insured" and can also add "reliable Repairs. Honest Service. Lasting Solutions" if spacing allows.

Other sections we would like included (not in any particular order):

-Why Choose KVT?:
Family-oriented team
Licensed & insured professionals
Residential & commercial expertise
Honest recommendations
Quality workmanship
Emergency service available
Clean, respectful technicians
One trusted company for plumbing and sewer solutions
____________________________
Our Story:
Built on solving complex plumbing challenges. Trusted for every plumbing need.
Since our founding, Conduit Renewal Partners has built a reputation for helping homeowners, businesses, and property managers solve some of the industry’s most challenging plumbing and sewer problems through quality workmanship, professionalism, and innovative solutions.
As our customers’ needs have grown, so has our commitment to serving them. What began as a leader in pipe restoration has expanded into full-service plumbing, allowing us to provide complete plumbing solutions—from everyday repairs and fixture replacements to water heaters, drain cleaning, repiping, and emergency plumbing services.
Today, our traditional plumbing division delivers the same level of expertise, communication, and customer care that KVT has become known for. Whether it’s a simple repair or a complex plumbing project, our goal remains the same: to provide dependable solutions, lasting quality, and an exceptional customer experience every step of the way.
-Our Values:
The KVT Way
Professional - Don't settle for good, BE GREAT
Responsive - When there's a need, BE FIRST!
Service - Life is not about you, BE ABOUT OTHERS!
These three values guide everything we do
Complete Plumbing Solutions:
-Plumbing Repairs
Reliable solutions to keep your plumbing system running safely and efficiently.
Leak detection & repair
Pipe Burst Repairs
Water line repairs
Whole-home repiping

-Fixtures & Installations
Professional installation, repair, and replacement of the fixtures you use every day.
Faucets
Toilets
Sinks
Showers & tubs
Garbage disposals
Hose bibs
Shut-off valves

-Water Heater Services
Whether you need a repair, replacement, or routine maintenance, we'll keep your hot water flowing.
Water heater repair
Water heater replacement
Tankless water heaters
Expansion tanks
Recirculation pumps
Preventative maintenance

-Drain & Sewer Solutions
From routine drain cleaning to complete sewer repairs, our team has the equipment and expertise to get your plumbing flowing again.
Drain cleaning
Hydro jetting
Camera inspections
Main sewer line cleaning
Sewer line repair
Sewer line replacement
Emergency drain backups
maybe add in a blurb saying
"Need a Trenchless Solution?
Ask about our non-invasive solutions as an alternative to traditional replacement for sewer and storm drain systems"
Testimonials:
"This company is fantastic, very professional and knowledgeable. Use them at several of my communities I manage and highly recommend them!" Belvine Townhomes
"KVT continues to be the primary plumbing vendor I use for all of my properties throughout Tampa Bay!" Corliss Dunes Condominium
"KVT did a great job at a great price and have always been willing to help with their abundance of knowledge prior to even working on projects for our community!" Townhomes at Hollow Fern
"KVT is amazing! My office flooded out on a Friday night and they responded within a couple hours to make the needed repair. The team was professional and got right to work (there van was also immaculate, which tells you a lot about hot they operate). Would definitely recommend them to anyone!" Dorin Welsby
______________________
Ready to get started?
Whether it's a leaking pipe, a new water heater, a clogged drain, or a plumbing emergency, our team is here to help
800-318-4957
info@kvtflow.example
www.kvtflow.example

Additional Information: please feel free to edit any of the pictures provided and AI files can be provided for the other marketing material if helpful. We would like an AI file and PDF ready print if possible.
Thank you!

commercial and residential property owners

Plumbing

Colors
0054AA
0677BA
7BADD7
CADEEF
E8F1F8

Must have
• My project must flow with current marketing material colors
Nice to have
• would like the front page picture to fade nicely into background

```html
<!DOCTYPE html>
<html lang="en">
<head>
<meta charset="utf-8">
<title>KVT Traditional Plumbing Services Trifold</title>
<link href="https://fonts.googleapis.com/css2?family=Poppins:wght@400;500;600;700;800&display=swap" rel="stylesheet">
<style>
:root{
  --navy:#1f3685;
  --sky:#3a9be3;
  --ink:#1b1b1b;
  --grey:#444444;
  --paper:#ffffff;
  --backdrop:#4b4b4b;
  --photo-dark:#5a5f66;
  --photo-mid:#8c9096;
}
*{margin:0;padding:0;box-sizing:border-box}
html,body{width:825px;height:1200px;overflow:hidden;background:var(--backdrop);font-family:"Poppins",sans-serif;color:var(--ink)}
.sheet{position:absolute;left:51px;width:722px;height:511px;background:var(--paper);overflow:hidden;box-shadow:0 10px 14px rgba(0,0,0,.35)}
.sheet-outside{top:65px}
.sheet-inside{top:618px}
.abs{position:absolute}

.photo{position:absolute;background:linear-gradient(160deg,var(--photo-mid),var(--photo-dark))}

/* Our Story */
.story-card{left:14px;top:182px;width:213px;height:329px;background:var(--paper);border-radius:10px 10px 0 0}
.story-title{left:28px;top:188px;font-size:20px;line-height:26px;font-weight:700;color:var(--navy)}
.story-lead{left:28px;top:216px;width:166px;font-size:8.4px;line-height:10.4px;font-weight:500}
.story-rule{left:28px;top:254px;width:46px;height:2px;background:var(--navy)}
.story-body{left:28px;top:266px;width:190px;font-size:6.5px;line-height:8.5px;text-align:justify}
.story-body p{margin-bottom:8px}
.web-line{left:28px;top:472px;font-size:8px;font-weight:500;display:flex;align-items:center;gap:4px}
.rule-line{height:1.5px;background:var(--navy)}

/* Ready */
.ready-title{left:262px;top:34px;font-size:25px;line-height:27.5px;font-weight:800;color:var(--navy)}
.ready-text{left:262px;top:128px;width:196px;font-size:9.2px;line-height:11.8px}
.contact-block{left:240.5px;top:372px;width:241px;height:139px;background:var(--navy);color:#fff;text-align:center}
.call-label{position:absolute;top:14px;width:100%;font-size:10px;font-weight:500}
.phone-pill{position:absolute;left:17.5px;top:36px;width:207px;height:29px;border:1.5px solid #fff;border-radius:15px;font-size:22px;font-weight:700;line-height:26px;letter-spacing:.3px}
.contact-row{position:absolute;top:75px;width:100%;font-size:7.8px;display:flex;justify-content:center;gap:10px}
.contact-row span{display:flex;align-items:center;gap:3px}

/* Cover */
.brand{left:504px;top:250px;display:flex;align-items:center;gap:5px;font-size:22px;font-weight:800;color:var(--navy);letter-spacing:1px}
.brand-mark{width:12px;height:12px;background:var(--sky)}
.cover-title{left:504px;top:290px;font-size:24px;line-height:26px;font-weight:600;color:var(--grey)}
.cover-title strong{display:block;color:var(--navy);font-weight:800}
.cover-rule{left:504px;top:376px;width:46px;height:2px;background:var(--navy)}
.cover-sub{left:504px;top:388px;font-size:12.5px;color:var(--grey)}
.emergency-pill{left:497px;top:408px;width:200px;height:27px;border-radius:14px;background:var(--navy);color:#fff;font-size:13.5px;font-weight:700;text-align:center;line-height:27px}
.cover-licensed{left:504px;top:443px;font-size:11px;color:var(--grey)}
.cover-tagline{right:36px;top:466px;font-size:6px;line-height:9px;font-weight:700;text-align:right;color:#222}

/* Why choose */
.why-panel{left:0;top:0;width:240.5px;height:223px;background:var(--navy);color:#fff}
.why-title{position:absolute;left:30px;top:22px;font-size:13.5px;font-weight:700;color:var(--sky)}
.why-list{position:absolute;left:28px;top:47px;width:180px;list-style:none}
.why-list li{position:relative;padding:3.6px 0 3.6px 11px;font-size:9px;line-height:11.6px;border-bottom:1px solid rgba(58,155,227,.55)}
.why-list li::before{content:"";position:absolute;left:2px;top:5px;width:3px;height:6px;border:solid var(--sky);border-width:0 1.5px 1.5px 0;transform:rotate(40deg)}
.trenchless{left:0;top:223px;width:240.5px;height:70px;background:var(--sky);color:#fff;padding:8px 0 0 28px}
.trenchless h3{font-size:12.8px;font-weight:700;line-height:16px}
.trenchless p{font-size:8.6px;line-height:11.4px;width:205px}

/* Solutions */
.solutions-title{left:249px;top:22px;font-size:13.5px;font-weight:700;color:var(--sky)}
.service-box{position:absolute;border:1px solid var(--navy);border-top:none;border-radius:0 0 7px 7px;background:#fff}
.service-head{position:absolute;left:-5px;top:0;right:0;height:14px;background:var(--navy);color:#fff;font-size:9.4px;font-weight:700;line-height:14px;padding-left:27px}
.service-head.alt{color:var(--sky)}
.service-head::before{content:"";position:absolute;left:0;top:-3px;width:18px;height:18px;border-radius:50%;background:var(--navy);border:1.5px solid #fff}
.service-intro{position:absolute;left:5px;top:17px;right:3px;font-size:7.7px;line-height:9.8px}
.service-list{position:absolute;left:7px;list-style:none;font-size:7.7px;line-height:13px}
.service-list li,.cols li{position:relative;padding-left:11px;white-space:nowrap}
.service-list li::before,.cols li::before{content:"";position:absolute;left:2px;top:2px;width:3px;height:6px;border:solid var(--sky);border-width:0 1.5px 1.5px 0;transform:rotate(40deg)}
.cols{position:absolute;left:7px;right:4px;display:flex;list-style:none;font-size:7.7px;line-height:10px}
.cols ul{list-style:none}
.cols .wrap li{white-space:normal}

/* Testimonials */
.testimonials{left:0;top:293px;width:481.5px;height:218px;background:linear-gradient(120deg,#4e535a,#7a7f86 55%,#5d6168)}
.testi-title{left:28px;top:303px;font-size:15.5px;font-weight:600;color:#fff}
.quote-card{position:absolute;background:#fff;border-radius:13px;padding:13px 12px 0 11px;font-size:6.8px;line-height:8.9px;color:#333}
.quote-card cite{position:absolute;right:17px;bottom:5px;font-style:normal;font-weight:700;color:var(--navy);font-size:6.8px}

/* Values */
.values{left:481.5px;top:293px;width:240.5px;height:218px;background:var(--navy);color:#fff}
.values-title{position:absolute;left:22.5px;top:12px;font-size:15.5px;font-weight:700;color:var(--sky)}
.values-way{position:absolute;left:22.5px;top:32px;font-size:8.4px}
.values-way b{color:var(--sky)}
.value{position:absolute;left:22.5px;display:flex;gap:8px;align-items:center}
.value h4{font-size:12.5px;line-height:14px;font-weight:700;color:var(--sky)}
.value p{font-size:8.8px;line-height:11px}
.value p b{font-weight:700}
.values-foot{position:absolute;left:22.5px;top:200px;font-size:8.2px;font-weight:700;font-style:italic}
</style>
</head>
<body>

<section class="sheet sheet-outside">
  <div class="photo" style="left:0;top:0;width:241px;height:201px" role="img" aria-label="Plumber working on pipes under a sink"></div>
  <div class="abs story-card"></div>
  <h2 class="abs story-title">Our Story</h2>
  <p class="abs story-lead">Built on solving complex plumbing challenges. Trusted for every plumbing need.</p>
  <div class="abs story-rule"></div>
  <div class="abs story-body">
    <p>Since our founding, Conduit Renewal Partners has built a reputation for helping homeowners, businesses, and property managers solve some of the industry’s most challenging plumbing and sewer problems through quality workmanship, professionalism, and innovative solutions.</p>
    <p>As our customers’ needs have grown, so has our commitment to serving them. What began as a leader in pipe restoration has expanded into full-service plumbing, allowing us to provide complete plumbing solutions—from everyday repairs and fixture replacements to water heaters, drain cleaning, repiping, and emergency plumbing services.</p>
    <p>Today, our traditional plumbing division delivers the same level of expertise, communication, and customer care that KVT has become known for. Whether it’s a simple repair or a complex plumbing project, our goal remains the same: to provide dependable solutions, lasting quality, and an exceptional customer experience every step of the way.</p>
  </div>
  <div class="abs web-line">
    <svg width="8" height="8" viewBox="0 0 10 10" fill="none" stroke="#1b1b1b" stroke-width="1"><circle cx="5" cy="5" r="4.3"/><ellipse cx="5" cy="5" rx="1.8" ry="4.3"/><path d="M.7 5h8.6"/></svg>
    www.kvtflow.example
  </div>
  <div class="abs rule-line" style="left:137px;top:478px;width:104px"></div>

  <h2 class="abs ready-title">Ready<br>to Get<br>Started?</h2>
  <p class="abs ready-text">Whether it's a leaking pipe, a new water heater, a clogged drain, or a plumbing emergency, our team is here to help.</p>
  <svg class="abs" style="left:240.5px;top:201px" width="241" height="171" role="img" aria-label="Hand adjusting a fitting on top of a water heater">
    <defs><linearGradient id="heaterTone" x1="0" y1="0" x2="1" y2="1"><stop offset="0" stop-color="#3c424c"/><stop offset="1" stop-color="#9aa2ad"/></linearGradient></defs>
    <path d="M0 0H197A44 44 0 0 1 241 44V171H0Z" fill="url(#heaterTone)"/>
  </svg>
  <div class="abs contact-block">
    <div class="call-label">Call Us for More Details</div>
    <div class="phone-pill">800-318-4957</div>
    <div class="contact-row">
      <span><svg width="8" height="6" viewBox="0 0 8 6"><rect width="8" height="6" rx=".6" fill="#fff"/><path d="M0 .5l4 3 4-3" stroke="#1f3685" stroke-width=".8" fill="none"/></svg>info@kvtflow.example</span>
      <span><svg width="8" height="8" viewBox="0 0 10 10" fill="none" stroke="#fff" stroke-width="1"><circle cx="5" cy="5" r="4.3"/><ellipse cx="5" cy="5" rx="1.8" ry="4.3"/><path d="M.7 5h8.6"/></svg>www.kvtflow.example</span>
    </div>
  </div>

  <svg class="abs" style="left:481.5px;top:0" width="241" height="300">
    <path d="M44 35H231V262L44 190Z" fill="#8a8d92" role="img" aria-label="Technician's hands connecting a water heater valve"/>
    <path d="M0 0H241V35H44V190L241 267V290L62 218Q0 194 0 150Z" fill="var(--navy)"/>
  </svg>
  <div class="abs brand"><span class="brand-mark"></span>KVT</div>
  <h1 class="abs cover-title">TRADITIONAL<strong>PLUMBING</strong><strong>SERVICES</strong></h1>
  <div class="abs cover-rule"></div>
  <div class="abs cover-sub">Residential &amp; Commercial</div>
  <div class="abs emergency-pill">24/7 Emergency Service</div>
  <div class="abs cover-licensed">Licensed &amp; Insured</div>
  <div class="abs cover-tagline">RELIABLE REPAIRS.<br>HONEST SERVICE.<br>LASTING SOLUTIONS.</div>
  <div class="abs rule-line" style="left:481.5px;top:478px;width:103px"></div>
</section>

<section class="sheet sheet-inside">
  <div class="abs why-panel">
    <h2 class="why-title">Why Choose KVT?</h2>
    <ul class="why-list">
      <li>Family-oriented team</li>
      <li>Licensed &amp; insured professionals</li>
      <li>Residential &amp; commercial expertise</li>
      <li>Honest recommendations</li>
      <li>Quality workmanship</li>
      <li>Emergency service available</li>
      <li>Clean, respectful technicians</li>
      <li>One trusted company for plumbing and sewer solutions</li>
    </ul>
  </div>
  <div class="abs trenchless">
    <h3>Need a Trenchless Solution?</h3>
    <p>Ask about our non-invasive solutions as an alternative to traditional replacement for sewer and storm drain systems.</p>
  </div>

  <h2 class="abs solutions-title">Complete Plumbing Solutions</h2>

  <div class="service-box" style="left:252px;top:48px;width:223px;height:104px">
    <div class="service-head">Plumbing Repairs</div>
    <p class="service-intro">Reliable solutions to keep your plumbing system running safely and efficiently.</p>
    <ul class="service-list" style="top:40px">
      <li>Leak Detection &amp; Repair</li><li>Pipe Burst Repairs</li><li>Water Line Repairs</li><li>Whole-Home Repiping</li>
    </ul>
  </div>
  <div class="service-box" style="left:492px;top:48px;width:211px;height:104px">
    <div class="service-head">Fixtures &amp; Installations</div>
    <p class="service-intro">Professional installation, repair, and replacement of the fixtures you use every day.</p>
    <div class="cols" style="top:40px">
      <ul style="width:94px"><li>Faucets</li><li>Toilets</li><li>Sinks</li><li>Showers &amp; Tubs</li><li>Garbage Disposals</li></ul>
      <ul><li>Hose Bibs</li><li>Shut-Off Valves</li></ul>
    </div>
  </div>
  <div class="service-box" style="left:252px;top:158px;width:223px;height:125px">
    <div class="service-head alt">Water Heater Services</div>
    <p class="service-intro">Whether you need a repair, replacement, or routine maintenance, we'll keep your hot water flowing.</p>
    <ul class="service-list" style="top:40px">
      <li>Water Heater Repair</li><li>Water Heater Replacement</li><li>Tankless Water Heaters</li><li>Expansion Tanks</li><li>Recirculation Pumps</li><li>Preventative Maintenance</li>
    </ul>
  </div>
  <div class="service-box" style="left:492px;top:158px;width:211px;height:125px">
    <div class="service-head">Drain &amp; Sewer Solutions</div>
    <p class="service-intro">From routine drain cleaning to complete sewer repairs, our team has the equipment and expertise to get your plumbing flowing again.</p>
    <div class="cols" style="top:50px;line-height:12.8px">
      <ul style="width:114px"><li>Drain Cleaning</li><li>Hydro Jetting</li><li>Camera Inspections</li><li>Main Sewer Line Cleaning</li><li>Sewer Line Repair</li></ul>
      <ul class="wrap" style="line-height:9.8px"><li>Sewer Line Replacement</li><li style="margin-top:6px">Emergency Drain Backups</li></ul>
    </div>
  </div>

  <div class="abs testimonials" role="img" aria-label="Faded photo of a plumbing team at work"></div>
  <h2 class="abs testi-title">Testimonials</h2>
  <blockquote class="quote-card" style="left:27px;top:331px;width:203px;height:60px">“This company is fantastic, very professional and knowledgeable. Use them at several of my communities I manage and highly recommend them!”<cite>— Belvine Townhomes</cite></blockquote>
  <blockquote class="quote-card" style="left:257px;top:331px;width:203px;height:60px">“KVT continues to be the primary plumbing vendor I use for all of my properties throughout Tampa Bay!”<cite>— Corliss Dunes Condominium</cite></blockquote>
  <blockquote class="quote-card" style="left:27px;top:399px;width:203px;height:91px;padding-top:21px">“KVT did a great job at a great price and have always been willing to help with their abundance of knowledge prior to even working on projects for our community!”<cite>— Dorin Welsby</cite></blockquote>
  <blockquote class="quote-card" style="left:257px;top:399px;width:203px;height:91px;padding-top:10px">“KVT is amazing! My office flooded out on a Friday night and they responded within a couple hours to make the needed repair. The team was professional and got right to work (their van was also immaculate, which tells you a lot about how they operate). Would definitely recommend them to anyone!”<cite>— Corliss Dunes Condominium</cite></blockquote>

  <div class="abs values">
    <h2 class="values-title">Our Values</h2>
    <div class="values-way">THE <b>KVT</b> WAY</div>
    <div class="value" style="top:50px">
      <svg width="24" height="24" viewBox="0 0 24 24" fill="none" stroke="#3a9be3" stroke-width="1.2"><circle cx="12" cy="12" r="11"/><path d="M12 5l2 4.2 4.6.6-3.3 3.2.8 4.6L12 15.4 7.9 17.6l.8-4.6L5.4 9.8 10 9.2Z"/></svg>
      <div><h4>Professional</h4><p>Don't settle for good,<br><b>BE GREAT.</b></p></div>
    </div>
    <div class="value" style="top:95px">
      <svg width="24" height="24" viewBox="0 0 24 24" fill="none" stroke="#3a9be3" stroke-width="1.2"><circle cx="12" cy="12" r="11"/><path d="M12 6v6h5"/></svg>
      <div><h4>Responsive</h4><p>When there's a need,<br><b>BE FIRST!</b></p></div>
    </div>
    <div class="value" style="top:141px">
      <svg width="24" height="24" viewBox="0 0 24 24" fill="none" stroke="#3a9be3" stroke-width="1.2"><circle cx="12" cy="12" r="11"/><path d="M12 17.5s-5.5-3.4-5.5-7A3 3 0 0 1 12 8.7a3 3 0 0 1 5.5 1.8c0 3.6-5.5 7-5.5 7Z"/></svg>
      <div><h4>Service</h4><p>Life is not about you,<br><b>BE ABOUT OTHERS!</b></p></div>
    </div>
    <p class="values-foot">These three values guide everything we do.</p>
  </div>
</section>

</body>
</html>
```